Business Card, A4 Letter Head and DL Envelope for Brandolux

We are looking for a design for our Business Card, A4 Letter Head and DL Envelope.

Brandolux is a distributor of promotional products. We specialize in a range of branded promotional products, these include pens, polo shirts, key rings, drink bottles, uniforms and bags to name a few. We are experts in marketing and assist companies in choosing the right promotional product for their needs. We will predominately be an online business where customers visit our website and browse our range of promotional products and branding options.

Our colours are black, red, white and grey.

Files must be supplied in eps, pdf and ai format.

Please display the following information:
Dorian Pell
Account Manager
Suite xxx, 214 Harwick Lane Melbourne, Victoria 3000
Phone +61 3 5550 1842
Mobile +61 455 501 736
sales@brandolux.example
www.brandolux.example

```html
<!DOCTYPE html>
<html lang="en">
<head>
<meta charset="utf-8">
<title>Brandolux Stationery</title>
<link href="https://fonts.googleapis.com/css2?family=Noto+Sans:wght@400;700&display=swap" rel="stylesheet">
<style>
  :root {
    --red: #d41920;
    --red-dark: #8e1216;
    --red-fade: rgba(212, 25, 32, 0);
    --grey-text: #8a8a8a;
    --ink: #222;
    --logo-grey: #5a5a5a;
    --paper: #ffffff;
    --bg-centre: #f4f4f4;
    --bg-edge: #d6d6d6;
    --flap-edge: #c8c8c8;
  }
  * { box-sizing: border-box; margin: 0; padding: 0; }
  html, body { width: 1200px; height: 900px; overflow: hidden; }
  body {
    position: relative;
    font-family: "Noto Sans", Arial, sans-serif;
    background: radial-gradient(ellipse at 50% 45%, var(--bg-centre) 0%, var(--bg-edge) 100%);
    color: var(--ink);
  }
  .sheet {
    position: absolute;
    background: var(--paper);
    box-shadow: 0 3px 10px rgba(0,0,0,.22);
    overflow: hidden;
  }
  address { font-style: normal; }

  /* soft colour band at the foot of each piece */
  .foot-band {
    position: absolute; left: 0; right: 0; bottom: 0;
    background: linear-gradient(to bottom, var(--red-fade) 0%, rgba(212,25,32,.55) 55%, var(--red) 85%, var(--red-dark) 100%);
  }

  /* brand lockup */
  .brand { position: absolute; display: flex; align-items: center; gap: 8px; }
  .brand-dot { border-radius: 50%; background: var(--red); flex: none; }
  .brand-name { font-weight: 700; color: var(--logo-grey); letter-spacing: .5px; }

  .contact {
    position: absolute; text-align: right; color: var(--grey-text);
    font-size: 7.6px; line-height: 10.4px;
  }

  /* letterhead */
  .letterhead { left: 62px; top: 86px; width: 509px; height: 717px; }
  .letterhead .brand { left: 40px; top: 100px; }
  .letterhead .brand-dot { width: 34px; height: 34px; }
  .letterhead .brand-name { font-size: 21px; }
  .letterhead .contact { right: 36px; top: 78px; }
  .letterhead .foot-band { height: 138px; }
  .letter { position: absolute; left: 61px; top: 183px; width: 388px; font-size: 8.9px; line-height: 13.2px; }
  .letter .recipient { margin-bottom: 13px; }
  .letter .salutation { margin-bottom: 13px; }
  .letter p.body { text-align: justify; margin-bottom: 13px; }
  .signature {
    width: 118px; height: 30px; margin-top: 10px;
    background: linear-gradient(90deg, rgba(40,50,140,.18), rgba(40,50,140,.05));
    border-radius: 4px;
  }
  .closing { margin-top: 6px; }

  /* business cards */
  .card-front { left: 615px; top: 85px; width: 220px; height: 133px;
    background: radial-gradient(ellipse at 50% 40%, #e12229 0%, var(--red) 45%, var(--red-dark) 100%); }
  .card-front .brand { left: 0; right: 0; top: 0; bottom: 0; flex-direction: column; justify-content: center; gap: 12px; padding-top: 6px; }
  .card-front .brand-dot { width: 36px; height: 36px; background: #ececec; }
  .card-front .brand-name { font-size: 14.5px; color: #e4e4e4; }

  .card-back { left: 852px; top: 85px; width: 218px; height: 133px; }
  .card-back .brand { left: 16px; top: 38px; gap: 5px; }
  .card-back .brand-dot { width: 17px; height: 17px; }
  .card-back .brand-name { font-size: 10px; }
  .card-back .contact { right: 15px; top: 16px; font-size: 5.2px; line-height: 7.3px; }
  .card-back .foot-band { height: 40px; }
  .card-person { position: absolute; left: 60px; width: 100px; top: 89px; text-align: center; }
  .card-person .name { color: var(--red); font-weight: 700; font-size: 8.6px; line-height: 11px; }
  .card-person .role { color: var(--grey-text); font-size: 6.2px; }

  /* envelope */
  .envelope-front { left: 613px; top: 260px; width: 533px; height: 265px; }
  .envelope-front .brand { left: 30px; top: 84px; }
  .envelope-front .brand-dot { width: 28px; height: 28px; }
  .envelope-front .brand-name { font-size: 17px; }
  .envelope-front .contact { right: 33px; top: 55px; }
  .envelope-front .foot-band { height: 120px; }

  .envelope-back { left: 613px; top: 540px; width: 533px; height: 266px; overflow: visible; background: none; box-shadow: none; }
  .envelope-back svg { position: absolute; left: 0; top: 0; filter: drop-shadow(0 3px 5px rgba(0,0,0,.2)); }
</style>
</head>
<body>

<!-- A4 letterhead -->
<section class="sheet letterhead">
  <div class="brand">
    <span class="brand-dot"></span>
    <span class="brand-name">BRANDOLUX</span>
  </div>
  <address class="contact">
    Suite XXX, 214 Harwick Lane,<br>
    Melbourne, Victoria 3000<br>
    Phone +61 3 5550 1842<br>
    sales@brandolux.example<br>
    www.brandolux.example
  </address>

  <div class="letter">
    <p class="recipient">Mara Quill<br>88 Fernbrook St<br>Oakridge MA</p>
    <p class="salutation">Dear Mrs Mara Quill,</p>
    <p class="body">Lorem ipsum dolor sit amet, consectetur adipiscing elit. Integer aliquet diam eget mi rutrum consectetur et id orci. Praesent vitae felis vitae justo elementum tincidunt. Duis pharetra turpis semper dui elementum nec aliquet lectus pulvinar. Donec condimentum mattis diam, id congue risus congue a. Maecenas commodo, nisi a gravida condimentum, elit erat condimentum leo, in pellentesque elit erat id nisi. Pellentesque consequat faucibus dictum. Nam tincidunt viverra elit at hendrerit. Quisque eget purus tellus. Mauris mattis nunc nec nisi pulvinar consectetur.</p>
    <p class="body">Nunc molestie iaculis orci, vitae consequat mi condimentum vitae. Etiam et tortor velit. Sed ac magna tellus. Proin quam augue, vehicula sed euismod in, vehicula eu felis. Pellentesque a orci ac turpis commodo varius at ut arcu. Integer viverra semper sapien fermentum egestas. Curabitur erat purus, congue et faucibus sit amet, fringilla elementum odio. Sed pretium tincidunt mi, nec fermentum urna interdum sed. Nam et lectus turpis, quis cursus ipsum. Maecenas non nibh odio. Sed in laoreet justo.</p>
    <p class="body">Aenean sed sem lacus. Vivamus auctor, sapien non aliquet ultrices, mauris turpis porttitor nisl, id rutrum velit erat non urna. Praesent eu augue eu ligula feugiat malesuada. Proin nec nibh erat. Sed et leo id leo volutpat viverra non ac mi. In quis dictum magna. Donec ut dui sed dui tristique dictum. Donec varius sapien sed turpis dictum a dignissim diam facilisis.</p>
    <div class="signature" role="img" aria-label="Handwritten signature of Dorian Pell"></div>
    <p class="closing">Yours Sincerely<br>Dorian Pell</p>
  </div>

  <div class="foot-band" role="img" aria-label="Red decorative wave graphic along the foot of the page"></div>
</section>

<!-- Business card, front -->
<section class="sheet card-front">
  <div class="brand">
    <span class="brand-dot"></span>
    <span class="brand-name">BRANDOLUX</span>
  </div>
</section>

<!-- Business card, back -->
<section class="sheet card-back">
  <div class="brand">
    <span class="brand-dot"></span>
    <span class="brand-name">BRANDOLUX</span>
  </div>
  <address class="contact">
    Suite XXX, 214 Harwick Lane,<br>
    Melbourne, Victoria 3000<br>
    Phone +61 3 5550 1842<br>
    Mobile +61 455 501 736<br>
    sales@brandolux.example<br>
    www.brandolux.example
  </address>
  <div class="card-person">
    <p class="name">Dorian Pell</p>
    <p class="role">Account Manager</p>
  </div>
  <div class="foot-band" role="img" aria-label="Red decorative wave graphic along the foot of the card"></div>
</section>

<!-- DL envelope, front -->
<section class="sheet envelope-front">
  <div class="brand">
    <span class="brand-dot"></span>
    <span class="brand-name">BRANDOLUX</span>
  </div>
  <address class="contact">
    Suite XXX, 214 Harwick Lane,<br>
    Melbourne, Victoria 3000<br>
    Phone +61 3 5550 1842<br>
    sales@brandolux.example<br>
    www.brandolux.example
  </address>
  <div class="foot-band" role="img" aria-label="Red decorative wave graphic along the foot of the envelope"></div>
</section>

<!-- DL envelope, back -->
<section class="sheet envelope-back">
  <svg width="533" height="266" viewBox="0 0 533 266" aria-hidden="true">
    <defs>
      <linearGradient id="flapRed" x1="0" x2="1">
        <stop offset="0" stop-color="#b8161c"/>
        <stop offset=".5" stop-color="#e11d25"/>
        <stop offset="1" stop-color="#9a1318"/>
      </linearGradient>
    </defs>
    <rect x="0" y="0" width="533" height="266" fill="#fff"/>
    <path d="M10,66 L42,266" stroke="#c8c8c8" stroke-width="1" fill="none"/>
    <path d="M523,66 L491,266" stroke="#c8c8c8" stroke-width="1" fill="none"/>
    <path d="M0,0 L533,0 L520,58 Q517,68 505,68 L28,68 Q16,68 13,58 Z" fill="url(#flapRed)"/>
    <circle cx="267" cy="35" r="18" fill="#ececec"/>
  </svg>
</section>

</body>
</html>
```